New Organic Medical Marijuana Packging Design

New Organic Grower needs a fresh new design for the retail package.
the idea is to incorporate a compostable materials and come up with the resealable pouch/baggy that can hold the medicine and maybe another compartment for the promotional material (like rolling papers).
Company name is Rudy's Organic. (rudy- Rudolph is the name of our guru grower who also spends a ton of time playing in the dirt).
Medicine will need to be visible (whole or partially )through the side of the pack. an idea attached..

```html
<!DOCTYPE html>
<html lang="en">
<head>
<meta charset="utf-8">
<title>Rudy's Organic – Retail Pouch</title>
<link rel="stylesheet" href="https://fonts.googleapis.com/css2?family=Righteous&family=Montserrat:wght@500&display=swap">
<style>
  :root {
    --backdrop: #dfe7ec;
    --pouch-red: #b10812;
    --pouch-red-dark: #8e0610;
    --pouch-red-light: #c81420;
    --label-green: #2aa63d;
    --ink-white: #ffffff;
    --bud-green: #4f6a2c;
    --bud-amber: #9a7a2c;
  }
  * { box-sizing: border-box; margin: 0; padding: 0; }
  html, body {
    width: 1200px;
    height: 840px;
    overflow: hidden;
    background: var(--backdrop);
  }
  .canvas {
    position: relative;
    width: 1200px;
    height: 840px;
  }
  .pouch-art {
    position: absolute;
    inset: 0;
  }
  .brand-name {
    position: absolute;
    left: 420px;
    top: 190px;
    width: 365px;
    height: 84px;
    display: flex;
    align-items: center;
    justify-content: center;
    font-family: "Righteous", sans-serif;
    font-weight: 400;
    font-size: 36px;
    letter-spacing: 1px;
    color: var(--ink-white);
    text-transform: uppercase;
    white-space: nowrap;
  }
  .product-facts {
    position: absolute;
    left: 520px;
    top: 635px;
    list-style: none;
    font-family: "Montserrat", sans-serif;
    font-weight: 500;
    font-size: 14px;
    line-height: 19.5px;
    color: var(--ink-white);
    white-space: nowrap;
  }
  .product-facts li::before {
    content: "•";
    margin-right: 6px;
  }
  .product-type {
    position: absolute;
    left: 482px;
    top: 716px;
    width: 253px;
    height: 58px;
    display: flex;
    align-items: center;
    justify-content: center;
    font-family: "Montserrat", sans-serif;
    font-weight: 500;
    font-size: 19px;
    color: var(--ink-white);
    white-space: nowrap;
  }
</style>
</head>
<body>
<main class="canvas">
  <svg class="pouch-art" width="1200" height="840" viewBox="0 0 1200 840">
    <defs>
      <linearGradient id="pouch-sheen" x1="0" y1="0" x2="1" y2="0">
        <stop offset="0" stop-color="var(--pouch-red-dark)"/>
        <stop offset="0.35" stop-color="var(--pouch-red-light)"/>
        <stop offset="0.75" stop-color="var(--pouch-red)"/>
        <stop offset="1" stop-color="var(--pouch-red-dark)"/>
      </linearGradient>
      <radialGradient id="bud-tones" cx="0.5" cy="0.5" r="0.6">
        <stop offset="0" stop-color="var(--bud-amber)"/>
        <stop offset="1" stop-color="var(--bud-green)"/>
      </radialGradient>
    </defs>

    <rect class="pouch-body" x="365" y="70" width="470" height="720" fill="url(#pouch-sheen)"/>
    <line class="zip-seal" x1="365" y1="158" x2="835" y2="158" stroke="var(--pouch-red-dark)" stroke-width="3"/>

    <polygon class="brand-banner" points="420,192 785,188 780,272 426,276" fill="var(--label-green)"/>

    <rect class="decor-area" role="img" aria-label="Decorative outlined cloud motif"
      x="650" y="308" width="172" height="148" rx="12" fill="var(--pouch-red)"/>

    <rect class="product-window" role="img" aria-label="Window showing the cannabis buds inside the pouch"
      x="460" y="345" width="290" height="225" rx="24" fill="url(#bud-tones)"/>

    <polygon class="type-banner" points="484,716 735,712 731,772 480,774" fill="var(--label-green)"/>
  </svg>

  <h1 class="brand-name">Rudy's Organic</h1>

  <ul class="product-facts">
    <li>weight information</li>
    <li>rolling paper included</li>
    <li>other information</li>
  </ul>

  <p class="product-type">medicinal marijuana</p>
</main>
</body>
</html>
```